Business Card/ Email Signature Design Project

I am an Interior Designer. I need a business card that looks sophisticated stylish but simple in design. My work covers space design/ interior architecture/ furniture design/ product development & styling.

I have a very specific brief and know mostly what I want. I'm hoping to work with someone who can translate my ideas.

My branding should have a strong focus on my name, the majority of my work is referral based.
I'm keen to keep a monochromatic colour scheme: dark charcoal/ black/ white/ embossing/ silver. I'm not suggesting we use all that I've listed, they are possible ideas at this stage. I will need to be mindful of printing costs an also how I make the design work across, cards, letter heads, email logo and web design.

Theory behind images sent below;
1-Rug Image_(minus boarder) I was thinking this image could be used on the back of the card with my contact details over. I like that the lines are almost hand drawn and start to look free form. It's a subtle contrast to a more formal front of the card with my name.
2_Tomas Ferle_I really like the orientation, the proportion of font on the card, the colour and the font. I like the lower case for my name and the upper case for 'Interior Design'. Not sure if it should be 'Interior Designer or Interior Design' at this stage, was leaning towards 'Interior Design'. Was thinking the 'i' and 'd' in my surname could be the colour eg 'silver'?? We can decide on this once we see it.

Look forward to hearing from you.
Cheers,
Saskia Bremond

Printing

Saskia Bremond Interior Design

```html
<!DOCTYPE html>
<html lang="en">
<head>
<meta charset="utf-8">
<title>Tomas Ferle Interior Design – Business Card</title>
<link rel="stylesheet" href="https://fonts.googleapis.com/css2?family=Open+Sans:wdth,wght@75..100,400..700&display=swap">
<style>
  :root {
    --backdrop: #e6e4e1;
    --charcoal: #3a3a3b;
    --charcoal-light: #4a4a4c;
    --charcoal-dark: #2c2c2d;
    --ink: #111111;
    --white: #ffffff;
    --rug-light: #8f8f8d;
    --rug-mid: #7a7a78;
    --rug-dark: #666664;
  }
  * { box-sizing: border-box; margin: 0; padding: 0; }
  html, body {
    width: 1200px;
    height: 1200px;
    overflow: hidden;
    background: var(--backdrop);
    font-family: "Open Sans", Arial, sans-serif;
  }
  .sheet {
    position: relative;
    width: 1200px;
    height: 1200px;
  }
  .card {
    position: absolute;
    left: 160px;
    width: 880px;
    height: 510px;
    overflow: hidden;
    box-shadow: 0 10px 28px rgba(0, 0, 0, 0.22);
  }
  .card--front { top: 70px; }
  .card--back  { top: 620px; }

  .card__surface {
    position: absolute;
    inset: 0;
  }
  .card--front .card__surface {
    background:
      radial-gradient(ellipse at 30% 20%, var(--charcoal-light), transparent 65%),
      linear-gradient(160deg, var(--charcoal) 0%, var(--charcoal-dark) 100%);
  }
  .card--back .card__surface {
    background:
      radial-gradient(ellipse at 70% 30%, var(--rug-light), transparent 70%),
      linear-gradient(200deg, var(--rug-mid) 0%, var(--rug-dark) 100%);
  }

  .card__name {
    position: absolute;
    left: 0;
    right: 0;
    text-align: center;
    font-weight: 400;
    font-size: 148px;
    line-height: 1;
    letter-spacing: -2px;
  }
  .card__role {
    position: absolute;
    left: 0;
    right: 0;
    text-align: center;
    font-weight: 400;
    font-size: 52px;
    line-height: 1;
    letter-spacing: 1px;
  }

  .card--front .card__name { top: 118px; color: var(--white); }
  .card--front .card__role { top: 262px; color: var(--ink); }

  .card--back .card__name { top: 36px; color: var(--ink); }
  .card--back .card__role {
    top: 175px;
    color: var(--white);
    font-weight: 600;
  }

  .contact {
    position: absolute;
    font-stretch: 75%;
    font-size: 38px;
    line-height: 1.2;
    color: var(--white);
    text-shadow: 0 0 2px var(--ink), 1px 1px 0 var(--ink), -1px -1px 0 var(--ink);
    letter-spacing: -0.5px;
    list-style: none;
  }
  .contact--postal { left: 30px; top: 262px; }
  .contact--online { left: 452px; top: 385px; }
</style>
</head>
<body>
<main class="sheet">

  <section class="card card--front" aria-label="Business card front">
    <div class="card__surface" role="img" aria-label="Dark charcoal quilted diamond texture"></div>
    <h1 class="card__name">tomas ferle</h1>
    <p class="card__role">INTERIOR DESIGN</p>
  </section>

  <section class="card card--back" aria-label="Business card back">
    <div class="card__surface" role="img" aria-label="Grey rug texture with free-form dark hand-drawn lines"></div>
    <h2 class="card__name">tomas ferle</h2>
    <p class="card__role">INTERIOR DESIGN</p>
    <ul class="contact contact--postal">
      <li>Address:P.O Box 274 Elmsford VIC.3190</li>
      <li>Email: interiors@saskiabremond.com</li>
    </ul>
    <ul class="contact contact--online">
      <li>Web: www.saskiabremond.com</li>
      <li>Mobile: 0455 610 482</li>
    </ul>
  </section>

</main>
</body>
</html>
```